Looking for a dynamic business card for a pizzeria.

A business card with our food, logo, and space for name, title, email, website, phone. The card should convey quality, unique, amazing. On the front, I envision food photo or photos with the owners names and contact information. On the back, more food with locations, website, facebook, twitter, instagram icons. It should look polished, not cartoonish, or plain.
Target Market(s)
upscale, local food buyers, 30-50 years in age.
Industry/Entity Type
Restaurant
Contact Information for Business Card
Business Name: Crustella, LLC
Website: www.crustellaovens.com
Back:
2 locations: (can list on the back of card)
1. Linden Park
2736 Marlow Street
Marston, WA 98411
360-555-0143
2. Cedar Ridge
1187 Pelham Street
Marston, WA 98416
360-555-0187
front:
EDITABLE space for
Business name
Person's Name
title
2nd title
Email address
cell-phone number
Requirements
Must have
- logo
- my food photo or photos (no watermarks showing)
- locations on back
- Person contact information on front
- full bleed

```html
<!DOCTYPE html>
<html lang="en">
<head>
<meta charset="utf-8">
<title>Crustella, LLC — Business Cards</title>
<link href="https://fonts.googleapis.com/css2?family=Open+Sans:wght@400;600;700&display=swap" rel="stylesheet">
<style>
  :root {
    --page-bg: #ece9e4;
    --brand-red: #c0212f;
    --brand-red-dark: #9c1722;
    --brand-green: #2e6a3e;
    --brand-green-dark: #1f4d2b;
    --paper: #ffffff;
    --photo-warm: #c7653a;
    --photo-cream: #e9d9c4;
    --shadow: rgba(0,0,0,0.22);
  }
  * { box-sizing: border-box; margin: 0; padding: 0; }
  html, body {
    width: 1200px; height: 913px; overflow: hidden;
    background: var(--page-bg);
    font-family: "Open Sans", Arial, sans-serif;
  }
  .sheet {
    position: relative; width: 1200px; height: 913px;
    display: flex; align-items: center; justify-content: center; gap: 40px;
  }
  .card {
    width: 540px; height: 309px; display: block;
    filter: drop-shadow(0 10px 18px var(--shadow));
  }
  .card text { font-family: "Open Sans", Arial, sans-serif; }
  .person-name { fill: var(--brand-green); font-weight: 700; font-size: 22px; }
  .person-title { fill: var(--brand-red); font-weight: 400; font-size: 13px; }
  .contact-line { fill: var(--brand-green); font-weight: 600; font-size: 13.5px; }
  .contact-icon { fill: none; stroke: var(--brand-red); stroke-width: 1.4; }
  .brand-mark { fill: none; stroke: var(--paper); stroke-width: 3; }
  .brand-name { fill: var(--paper); font-weight: 700; font-size: 34px; letter-spacing: 2px; }
  .brand-legal { fill: var(--paper); font-weight: 700; font-size: 24px; }
  .location-line { fill: var(--paper); font-weight: 600; font-size: 13px; }
</style>
</head>
<body>
<main class="sheet">

  <svg class="card card-front" viewBox="0 0 540 309" xmlns="http://www.w3.org/2000/svg">
    <defs>
      <clipPath id="front-shape"><rect width="540" height="309" rx="16"/></clipPath>
      <linearGradient id="red-fill" x1="0" y1="0" x2="1" y2="1">
        <stop offset="0" stop-color="var(--brand-red)"/>
        <stop offset="1" stop-color="var(--brand-red-dark)"/>
      </linearGradient>
    </defs>
    <g clip-path="url(#front-shape)">
      <rect class="front-band" width="540" height="309" fill="url(#red-fill)"/>
      <path class="front-panel" d="M190,0 H540 V282 C380,282 196,200 190,0 Z" fill="var(--paper)"/>
      <path class="front-divider" d="M190,0 C196,200 380,282 540,282" fill="none" stroke="var(--brand-green)" stroke-width="6"/>
    </g>

    <g class="contact-block" text-anchor="end">
      <text class="person-name" x="490" y="66">MARCO BELLINI</text>
      <text class="person-title" x="490" y="86">Director, President</text>
      <text class="contact-line" x="472" y="112">360-555-0119</text>
      <text class="contact-line" x="472" y="133">marco@bellinimail.com</text>
      <text class="contact-line" x="472" y="154">www.crustellaovens.com</text>
    </g>
    <g class="contact-icons">
      <path class="contact-icon" d="M480,102 c-1,3 1,8 6,10 l2,-2 -2,-2 -1,1 c-2,-1 -3,-3 -3,-4 l1,-1 -2,-2 z"/>
      <rect class="contact-icon" x="479" y="124" width="11" height="8" rx="1"/>
      <path class="contact-icon" d="M479,124 l5.5,4.5 5.5,-4.5"/>
      <circle class="contact-icon" cx="484.5" cy="149.5" r="5.5"/>
      <path class="contact-icon" d="M479,149.5 h11 M484.5,144 c-3,3 -3,8 0,11 c3,-3 3,-8 0,-11"/>
    </g>

    <g class="brand-lockup">
      <circle class="brand-mark" cx="56" cy="180" r="14"/>
      <text class="brand-name" x="40" y="230">CRUSTELLA</text>
      <text class="brand-legal" x="40" y="262">CRUSTELLA, LLC</text>
    </g>
  </svg>

  <svg class="card card-back" viewBox="0 0 540 309" xmlns="http://www.w3.org/2000/svg">
    <defs>
      <clipPath id="back-shape"><rect width="540" height="309" rx="16"/></clipPath>
      <linearGradient id="green-fill" x1="0" y1="0" x2="1" y2="1">
        <stop offset="0" stop-color="var(--brand-green)"/>
        <stop offset="1" stop-color="var(--brand-green-dark)"/>
      </linearGradient>
      <linearGradient id="photo-fill" x1="0" y1="1" x2="1" y2="0">
        <stop offset="0" stop-color="#5a3a2a"/>
        <stop offset="0.45" stop-color="var(--photo-warm)"/>
        <stop offset="1" stop-color="var(--photo-cream)"/>
      </linearGradient>
    </defs>
    <g clip-path="url(#back-shape)">
      <rect class="back-band" width="540" height="309" fill="url(#green-fill)"/>
      <path class="food-photo" role="img" aria-label="Photo of freshly baked pizza rolls with tomato topping"
            d="M150,309 C230,150 380,78 540,70 V309 Z" fill="url(#photo-fill)"/>
      <path class="back-divider" d="M150,309 C230,150 380,78 540,70" fill="none" stroke="var(--paper)" stroke-width="6"/>
    </g>

    <g class="brand-lockup">
      <circle class="brand-mark" cx="46" cy="80" r="14"/>
      <text class="brand-name" x="30" y="130">CRUSTELLA</text>
      <text class="brand-legal" x="30" y="162">CRUSTELLA, LLC</text>
    </g>

    <g class="locations" text-anchor="end">
      <text class="location-line" x="510" y="160">360-555-0143</text>
      <text class="location-line" x="510" y="178">Linden Park 2736 Marlow</text>
      <text class="location-line" x="510" y="196">Street Marston, WA 98411</text>
      <text class="location-line" x="510" y="222">360-555-0187</text>
      <text class="location-line" x="510" y="240">Cedar Ridge 1187 Pelham</text>
      <text class="location-line" x="510" y="258">Street Marston, WA 98416</text>
    </g>
  </svg>

</main>
</body>
</html>
```